The Perfect Business Card for Tavoranth

I am looking for a business card which beautifully incorporates my logo, reflects my business and looks special, elegant and clean.

```html
<!DOCTYPE html>
<html lang="en">
<head>
<meta charset="utf-8">
<title>Tavoranth Business Card</title>
<link rel="stylesheet" href="https://fonts.googleapis.com/css2?family=Poppins:wght@400;500&display=swap">
<style>
  :root {
    --backdrop: #e4e7e3;
    --card: #ffffff;
    --olive: #5a7a2b;
    --leaf: #8db545;
    --ink: #2b2b2b;
    --faint: #e6e9df;
  }
  * { margin: 0; padding: 0; box-sizing: border-box; }
  html, body { width: 1200px; height: 900px; overflow: hidden; }
  body {
    background: var(--backdrop);
    font-family: "Poppins", sans-serif;
    position: relative;
  }
  .card {
    position: absolute;
    left: 300px;
    width: 600px;
    height: 343px;
    background: var(--card);
    box-shadow: 0 10px 30px rgba(0,0,0,0.12);
    overflow: hidden;
  }
  .card-info { top: 90px; }
  .card-brand { top: 470px; }

  .brand {
    display: flex;
    align-items: center;
    gap: 10px;
    color: var(--olive);
    font-weight: 500;
    letter-spacing: 0.08em;
  }
  .brand-dot {
    border: 2px solid var(--olive);
    border-radius: 50%;
  }
  .card-info .brand { position: absolute; top: 34px; right: 42px; font-size: 22px; }
  .card-info .brand-dot { width: 46px; height: 46px; }

  .divider {
    position: absolute;
    top: 118px;
    left: 268px;
    right: 0;
    height: 2px;
    background: var(--leaf);
  }
  .faint-circle {
    position: absolute;
    top: 140px;
    right: 44px;
    width: 110px;
    height: 110px;
    border: 2px solid var(--faint);
    border-radius: 50%;
  }

  .person { position: absolute; left: 40px; top: 100px; padding-left: 0; }
  .person-name {
    font-size: 25px;
    font-weight: 400;
    color: var(--olive);
    line-height: 1.1;
  }
  .person-role { font-size: 14px; color: var(--ink); margin-top: 2px; }
  .accent-block {
    position: absolute;
    left: 0;
    top: 106px;
    width: 28px;
    height: 42px;
    background: var(--leaf);
  }
  .contacts {
    position: absolute;
    left: 40px;
    top: 200px;
    list-style: none;
    font-size: 13px;
    color: var(--ink);
  }
  .contacts li { display: flex; align-items: center; gap: 12px; line-height: 24px; }
  .contacts svg { width: 12px; height: 12px; fill: var(--olive); flex: none; }

  .card-brand .brand {
    position: absolute;
    left: 50%;
    top: 50%;
    transform: translate(-50%, -50%);
    font-size: 44px;
    gap: 18px;
  }
  .card-brand .brand-dot { width: 100px; height: 100px; }
</style>
</head>
<body>
  <section class="card card-info">
    <div class="brand"><span class="brand-dot"></span><span class="brand-name">TAVORANTH</span></div>
    <div class="divider"></div>
    <div class="faint-circle"></div>
    <div class="accent-block"></div>
    <div class="person">
      <h1 class="person-name">Daniel Varga</h1>
      <p class="person-role">Chief Executive</p>
    </div>
    <ul class="contacts">
      <li><svg viewBox="0 0 24 24"><path d="M6.6 10.8a15 15 0 0 0 6.6 6.6l2.2-2.2a1 1 0 0 1 1-.25 11.4 11.4 0 0 0 3.6.57 1 1 0 0 1 1 1V20a1 1 0 0 1-1 1A17 17 0 0 1 3 4a1 1 0 0 1 1-1h3.5a1 1 0 0 1 1 1c0 1.25.2 2.45.57 3.57a1 1 0 0 1-.25 1z"/></svg>+420 604 219 557</li>
      <li><svg viewBox="0 0 24 24"><path d="M2 5h20v14H2z M2 5l10 8 10-8" /></svg>info@tavoranth.com</li>
      <li><svg viewBox="0 0 24 24"><path d="M12 2a10 10 0 1 0 0 20 10 10 0 0 0 0-20zm0 2c1.5 1.8 2.3 4.3 2.4 7H9.6c.1-2.7.9-5.2 2.4-7zm-2.4 9h4.8c-.1 2.7-.9 5.2-2.4 7-1.5-1.8-2.3-4.3-2.4-7zM4.1 11a8 8 0 0 1 4.4-6.3A13 13 0 0 0 7.6 11zm0 2h3.5a13 13 0 0 0 .9 6.3A8 8 0 0 1 4.1 13zm12.3 0h3.5a8 8 0 0 1-4.4 6.3 13 13 0 0 0 .9-6.3zm0-2a13 13 0 0 0-.9-6.3 8 8 0 0 1 4.4 6.3z"/></svg>www.tavoranth.com</li>
      <li><svg viewBox="0 0 24 24"><path d="M12 2a7 7 0 0 0-7 7c0 5 7 13 7 13s7-8 7-13a7 7 0 0 0-7-7zm0 9.5A2.5 2.5 0 1 1 12 6.5a2.5 2.5 0 0 1 0 5z"/></svg>Lipova 14, 120 00 Praha 2</li>
    </ul>
  </section>

  <section class="card card-brand">
    <div class="brand"><span class="brand-dot"></span><span class="brand-name">TAVORANTH</span></div>
  </section>
</body>
</html>
```